2018 Fundraiser Event Flier

We are a non profit that works in the homeless community, The Lanternbrook Alliance. We offer a unique program of supported employment that is all about community engagement and building relationships not only with our participants but with community businesses and non profit partners. Our mission statement is "We seek and foster partnerships between the business and nonprofit communities to respectfully and effectively guide individuals from disenfranchised communities forward in sustainable employment to realize their potential of fully enriched lives for themselves and their families" We are having a fundraising event on Dec 13 and need a flier to advertise the event both via email and physical postings. We like a black background and bright colors (see uploaded example) and want to advertise the event and a small amount about who we are. Fun and bright. We will upload two of our logos and two photos that we have used in branding previously.

```html
<!DOCTYPE html>
<html lang="en">
<head>
<meta charset="utf-8">
<title>The Lanternbrook Alliance – Fundraising Flier</title>
<link rel="stylesheet" href="https://fonts.googleapis.com/css2?family=Exo+2:wght@300;500;600&family=Oswald:wght@600&family=Roboto:wght@400;700&display=swap">
<style>
  :root{
    --page:#e9e9e9;
    --ink:#14161a;
    --white:#ffffff;
    --gold:#f7b500;
    --orange:#ff5a00;
    --blue:#00bfe8;
    --purple:#5b1596;
    --yellow:#ffd000;
    --hatch:#9ff0f3;
  }
  *{box-sizing:border-box;margin:0;padding:0}
  html,body{width:1200px;height:1000px;overflow:hidden;background:var(--page)}
  .canvas{position:relative;width:1200px;height:1000px}
  .flier{
    position:absolute;left:220px;top:8px;width:755px;height:977px;
    background:var(--ink);overflow:hidden;
    box-shadow:0 2px 8px rgba(0,0,0,.35);
    font-family:"Roboto",Arial,sans-serif;color:var(--white);
  }
  .bands{position:absolute;inset:0}
  .brand{
    position:absolute;left:0;right:0;top:226px;text-align:center;
    font-family:"Exo 2",sans-serif;font-weight:600;color:var(--white);
    text-transform:uppercase;line-height:1.1;
  }
  .brand .line1{font-size:44px;letter-spacing:1px;display:block}
  .brand .line2{font-size:40px;letter-spacing:3px;display:block}
  .event-title{
    position:absolute;left:0;right:0;top:336px;text-align:center;
    font-family:"Exo 2",sans-serif;font-weight:300;font-size:58px;
    color:var(--gold);letter-spacing:1px;line-height:70px;
  }
  .event-rule{position:absolute;left:195px;width:360px;top:401px;height:3px;background:var(--gold)}
  .event-date{
    position:absolute;left:0;right:0;top:414px;text-align:center;
    font-weight:700;font-size:24px;letter-spacing:.5px;line-height:28px;
  }
  .section-tab{position:absolute;left:245px;top:480px;width:262px;height:62px}
  .section-tab span{
    position:absolute;left:0;top:0;width:262px;height:42px;line-height:42px;text-align:center;
    font-family:"Oswald",sans-serif;font-weight:600;font-size:27px;color:var(--ink);
  }
  .about{
    position:absolute;left:98px;width:566px;top:557px;
    font-size:16.4px;line-height:22px;
  }
  .mission{text-align:justify;text-align-last:left}
  .program{margin-top:9px;text-align:center}
  .partners{
    position:absolute;left:130px;right:120px;top:756px;display:flex;
    justify-content:space-between;align-items:center;
  }
  .partner{
    font-family:"Roboto",Arial,sans-serif;font-weight:400;font-size:15px;
    color:var(--white);text-align:center;line-height:1.2;width:150px;
  }
  .partner.middle{width:120px}
</style>
</head>
<body>
<div class="canvas">
  <div class="flier">
    <svg class="bands" width="755" height="977" viewBox="220 8 755 977" aria-hidden="true">
      <defs><clipPath id="sheet"><rect x="220" y="8" width="755" height="977"/></clipPath></defs>
      <g clip-path="url(#sheet)" stroke-linecap="butt" fill="none">
        <line x1="200" y1="10" x2="350" y2="160" stroke="var(--blue)" stroke-width="42"/>
        <line x1="250" y1="50" x2="330" y2="130" stroke="var(--hatch)" stroke-width="30" opacity=".55"/>
        <line x1="300" y1="-10" x2="450" y2="140" stroke="var(--purple)" stroke-width="44"/>
        <line x1="200" y1="100" x2="310" y2="210" stroke="var(--orange)" stroke-width="46"/>
        <line x1="260" y1="215" x2="460" y2="15" stroke="var(--orange)" stroke-width="44"/>
        <line x1="200" y1="150" x2="250" y2="200" stroke="var(--yellow)" stroke-width="40"/>
        <line x1="630" y1="-10" x2="870" y2="230" stroke="var(--yellow)" stroke-width="42"/>
        <line x1="820" y1="110" x2="900" y2="190" stroke="var(--hatch)" stroke-width="30" opacity=".55"/>
        <line x1="730" y1="-10" x2="990" y2="250" stroke="var(--orange)" stroke-width="48"/>
        <line x1="800" y1="-10" x2="990" y2="180" stroke="var(--blue)" stroke-width="42"/>
        <line x1="920" y1="-10" x2="990" y2="60" stroke="var(--purple)" stroke-width="44"/>
        <rect x="220" y="770" width="80" height="215" fill="var(--yellow)" opacity=".22"/>
        <line x1="230" y1="1000" x2="400" y2="830" stroke="var(--orange)" stroke-width="46"/>
        <line x1="340" y1="1000" x2="470" y2="850" stroke="var(--yellow)" stroke-width="44"/>
        <line x1="380" y1="860" x2="520" y2="1000" stroke="var(--orange)" stroke-width="40"/>
        <line x1="430" y1="880" x2="560" y2="1010" stroke="var(--purple)" stroke-width="40"/>
        <line x1="470" y1="850" x2="610" y2="990" stroke="var(--blue)" stroke-width="46"/>
        <line x1="530" y1="860" x2="670" y2="1000" stroke="var(--purple)" stroke-width="44"/>
        <line x1="700" y1="1000" x2="990" y2="700" stroke="var(--hatch)" stroke-width="40" opacity=".5"/>
        <line x1="860" y1="1010" x2="990" y2="880" stroke="var(--orange)" stroke-width="48"/>
      </g>
    </svg>

    <h1 class="brand"><span class="line1">The Lanternbrook</span><span class="line2">Alliance</span></h1>

    <h2 class="event-title">FUNDRAISING</h2>
    <div class="event-rule"></div>
    <p class="event-date">DECEMBER 13, 2018</p>

    <div class="section-tab">
      <svg width="262" height="62" viewBox="0 0 262 62" aria-hidden="true">
        <path d="M8 0 H254 A8 8 0 0 1 262 8 V60 L238 42 H8 A8 8 0 0 1 0 34 V8 A8 8 0 0 1 8 0 Z" fill="var(--gold)"/>
      </svg>
      <span>WHAT DO WE DO?</span>
    </div>

    <div class="about">
      <p class="mission">We seek and foster partnerships between the business and nonprofit communities to respectfully and effectively guide individuals from disenfranchised communities forward in sustainable employment to realize their potential of fully enriched lives for themselves and their families.</p>
      <p class="program">TLA provides this support through the placement of Peer Mentor or Trainers in the workforce creating a safe and dynamic training workspace within the business operations of our Community Partners:</p>
    </div>

    <div class="partners">
      <div class="partner">Harborline Visitor Services</div>
      <div class="partner middle">Mesa Ridge Wildlife Park</div>
      <div class="partner">Alder Grand Hotel</div>
    </div>
  </div>
</div>
</body>
</html>
```